Computer Company needs a Business card design

We need a business card design for our business. We assist people to transition to the QTG (Quillary Telelink Grid). The Australian Government-owned qtg™ network is a brand new telecommunications network currently being rolled out across Australia, giving access to a reliable broadband connection. Our niche market will predominantly be domestic customers in the 50+ age bracket. The assistance that we provide is everything from arranging the equipment, arranging the plan and contract term, appointment times, final testing of the network and any tweaks that need to be made. We basically PM the transition from start to finish. The business card design should be minimalist, should communicate loyalty and stability, should be easy to read and clearly explain what we do. We have asked for front and back. However, the back of the card does not have to include much information at all. It could be just a small design, or a repeat of our phone number. Up to you. The attached file only says what is required on the card. It does not specify where to arrange the text, what fonts to use, etc etc. As much as we would like to give you more info, due to our very limited design ability, we are not really able to send you any rough, or otherwise, designs of what we are after. Hopefully the above description is enough for you.

```html
<!DOCTYPE html>
<html lang="en">
<head>
<meta charset="utf-8">
<title>Connia Business Card – Front and Back</title>
<link rel="stylesheet" href="https://fonts.googleapis.com/css2?family=Open+Sans:wght@400;700&display=swap">
<style>
  :root {
    --backdrop: #2a2a2a;
    --card-light: #ececec;
    --card-dark: #161616;
    --ink: #1c1c1c;
    --ink-soft: #2b2b2b;
    --accent: #3b8dbd;
    --paper-white: #e8ecef;
  }
  * { margin: 0; padding: 0; box-sizing: border-box; }
  html, body {
    width: 1200px;
    height: 600px;
    overflow: hidden;
    background: var(--backdrop);
    font-family: "Open Sans", Arial, sans-serif;
  }
  .card {
    position: absolute;
    top: 165px;
    width: 466px;
    height: 271px;
    border-radius: 16px;
  }
  .card--front { left: 120px; background: var(--card-light); }
  .card--back  { left: 614px; background: var(--card-dark); }

  .brand {
    position: absolute;
    display: flex;
    align-items: center;
    gap: 8px;
    font-weight: 400;
    line-height: 1;
    white-space: nowrap;
  }
  .brand__dot {
    border-radius: 50%;
    background: var(--accent);
    flex: none;
  }
  .card--front .brand {
    right: 250px;
    top: 120px;
    font-size: 44px;
    color: var(--ink);
  }
  .card--front .brand__dot { width: 10px; height: 10px; }

  .divider {
    position: absolute;
    left: 237px;
    top: 81px;
    width: 2px;
    height: 125px;
    background: var(--accent);
  }
  .contact {
    position: absolute;
    left: 254px;
    top: 99px;
    color: var(--ink-soft);
  }
  .contact__name {
    font-size: 19px;
    font-weight: 400;
    margin-bottom: 10px;
    color: var(--ink);
  }
  .contact__name strong { font-weight: 700; }
  .contact__line {
    display: flex;
    align-items: center;
    gap: 7px;
    font-size: 12.5px;
    margin-bottom: 6px;
  }
  .contact__icon { width: 13px; height: 11px; flex: none; }

  .card--back .brand {
    left: 50%;
    top: 118px;
    transform: translateX(-50%);
    font-size: 54px;
    color: var(--paper-white);
  }
  .card--back .brand__dot { width: 12px; height: 12px; }
  .website {
    position: absolute;
    left: 0;
    right: 0;
    top: 214px;
    text-align: center;
    font-size: 11px;
    color: var(--accent);
    letter-spacing: 0.1px;
  }
</style>
</head>
<body>
  <section class="card card--front" aria-label="Card front">
    <div class="brand">
      <span class="brand__dot"></span>
      <span class="brand__name">Connia</span>
    </div>
    <div class="divider"></div>
    <div class="contact">
      <p class="contact__name">Rowan <strong>Ellery</strong></p>
      <p class="contact__line">
        <svg class="contact__icon" viewBox="0 0 13 11" aria-hidden="true">
          <path d="M1 3.2 C3 0.6 10 0.6 12 3.2 L10.6 4.6 L8.8 3.6 L8.8 2.6 C7.4 2.1 5.6 2.1 4.2 2.6 L4.2 3.6 L2.4 4.6 Z" fill="var(--accent)"/>
          <path d="M3.2 5 L9.8 5 L11.2 10 L1.8 10 Z" fill="var(--accent)"/>
          <circle cx="6.5" cy="7.4" r="1.3" fill="var(--card-light)"/>
        </svg>
        0491570286
      </p>
      <p class="contact__line">
        <svg class="contact__icon" viewBox="0 0 13 11" aria-hidden="true">
          <rect x="0.5" y="1.5" width="12" height="8.5" fill="var(--accent)"/>
          <path d="M0.8 1.8 L6.5 6.5 L12.2 1.8" fill="none" stroke="var(--card-light)" stroke-width="1"/>
        </svg>
        hello@conniahelp.com
      </p>
    </div>
  </section>

  <section class="card card--back" aria-label="Card back">
    <div class="brand">
      <span class="brand__dot"></span>
      <span class="brand__name">Connia</span>
    </div>
    <p class="website">www.conniahelp.com.au</p>
  </section>
</body>
</html>
```